Voyage Wellness Point Business Cards

We need business cards for our new start-up online travel health clinic. Visit our website voyagewellpoint.ca for branding and more info.

Target Market(s)

Travellers

Industry/Entity Type

Business

Contact Information for Business Card

Mara Kowalczyk
mara@voyagewellpoint.ca
+1 555 283 0461
voyagewellpoint.ca

Font styles to use
Sans Serif

Colors
f68d4d

```html
<!DOCTYPE html>
<html lang="en">
<head>
<meta charset="utf-8">
<title>Voyage Wellness Point – Business Cards</title>
<link href="https://fonts.googleapis.com/css2?family=Roboto:wght@400;700&display=swap" rel="stylesheet">
<style>
  :root{
    --orange:#f68d4d;
    --charcoal:#333333;
    --ink:#1e1e1e;
    --paper:#ffffff;
    --backdrop:#e7e5e2;
  }
  *{margin:0;padding:0;box-sizing:border-box}
  html,body{width:1200px;height:1000px;overflow:hidden}
  body{background:var(--backdrop);font-family:"Roboto",Arial,sans-serif;position:relative}
  .card{position:absolute;width:560px;height:320px;border-radius:22px;box-shadow:0 10px 28px rgba(0,0,0,.18)}
  .card--front{left:80px;top:110px;background:var(--charcoal);display:flex;align-items:center;justify-content:center}
  .card--back{left:560px;top:560px;background:var(--paper)}
  .brand{display:flex;align-items:center;gap:10px;color:var(--orange);font-weight:400;white-space:nowrap}
  .brand__dot{width:14px;height:14px;border-radius:50%;background:var(--orange);flex:none}
  .card--front .brand{font-size:40px}
  .card--back .brand{position:absolute;right:30px;top:150px;font-size:25px}
  .person{position:absolute;left:36px;top:190px;display:flex;align-items:center;gap:8px;font-weight:700;font-size:19px;letter-spacing:.3px}
  .person__first{color:var(--ink)}
  .person__last{color:var(--orange)}
  .contacts{position:absolute;left:40px;top:236px;list-style:none;font-size:14px;color:var(--ink);line-height:23px}
  .contacts li{display:flex;align-items:center;gap:8px}
  .contacts svg{width:13px;height:13px;flex:none}
  .web-accent{color:var(--orange);font-weight:700}
</style>
</head>
<body>
  <section class="card card--front">
    <div class="brand"><span class="brand__dot"></span>Voyage Wellness Point</div>
  </section>

  <section class="card card--back">
    <div class="brand"><span class="brand__dot"></span>Voyage Wellness Point</div>

    <div class="person">
      <svg width="12" height="14" viewBox="0 0 12 14"><polygon points="0,0 12,7 0,14" fill="var(--orange)"/></svg>
      <span class="person__first">MARA</span><span class="person__last">KOWALCZYK</span>
    </div>

    <ul class="contacts">
      <li>
        <svg viewBox="0 0 14 14"><rect x="1" y="3" width="12" height="9" rx="1" fill="var(--orange)"/><polyline points="1.5,3.5 7,8 12.5,3.5" fill="none" stroke="#fff" stroke-width="1.2"/></svg>
        mara@voyagewellpoint.ca
      </li>
      <li>
        <svg viewBox="0 0 14 14"><path d="M3 1.5l2.2 2.6-1.3 1.6c.9 1.8 2.3 3.2 4.1 4.1l1.6-1.3 2.6 2.2-1.4 1.8C6 12.5 1.5 8 1.2 2.9z" fill="var(--orange)"/></svg>
        +1 555 283 0461
      </li>
      <li>
        <svg viewBox="0 0 14 14"><circle cx="7" cy="7" r="6" fill="var(--orange)"/><ellipse cx="7" cy="7" rx="2.6" ry="6" fill="none" stroke="#fff" stroke-width="1"/><line x1="1" y1="7" x2="13" y2="7" stroke="#fff" stroke-width="1"/></svg>
        <span>www.<span class="web-accent">voyagewellpoint</span>.ca</span>
      </li>
    </ul>
  </section>
</body>
</html>
```